Construction Company

Design a clutter free business card, it can be double-sided utilizing the logo for BDN Ltd simple with all relevant contact information.

Please also a letterhead design to function for the purposes of invoicing, all mail requirements, with header to be distinctive while the footer ties page together and incorporates all necessary information.

For now, please use generic / dummy text and when a winner is selected, I will disclose the contact information.

Hi Designers! Please read the updated brief which includes the design of a business card and letterhead. Thank you!

```html
<!DOCTYPE html>
<html lang="en">
<head>
<meta charset="utf-8">
<title>BDN Ltd Letterhead</title>
<link href="https://fonts.googleapis.com/css2?family=Montserrat:wght@400;500;600;700&display=swap" rel="stylesheet">
<style>
  :root {
    --navy: #1f3a84;
    --gold: #b8962e;
    --ink: #111111;
    --paper: #ffffff;
    --sky: #b4dfee;
    --page-bg: #ffffff;
  }
  * { margin: 0; padding: 0; box-sizing: border-box; }
  html, body {
    width: 1200px;
    height: 2399px;
    overflow: hidden;
    background: var(--page-bg);
    font-family: "Montserrat", sans-serif;
  }
  .canvas { position: relative; width: 1200px; height: 2399px; }

  .backdrop {
    position: absolute;
    left: 0; top: 1198px;
    width: 1200px; height: 1201px;
    background: var(--sky);
  }

  .letterhead {
    position: absolute;
    width: 706px;
    height: 999px;
    background: var(--paper);
    border: 1px solid #d6d6d6;
    box-shadow: 4px 6px 8px rgba(0,0,0,0.22);
    overflow: hidden;
    transform-origin: top left;
  }
  .letterhead--primary { left: 247px; top: 100px; }
  .letterhead--secondary { left: 290px; top: 1329px; transform: scale(0.836); box-shadow: none; border: none; }

  .brand {
    position: absolute;
    left: 74px; top: 92px;
    display: flex; align-items: center; gap: 12px;
  }
  .brand-mark { width: 22px; height: 22px; background: var(--gold); }
  .brand-name {
    font-size: 46px; font-weight: 700; color: var(--navy);
    letter-spacing: 1px; line-height: 1;
  }

  .letter {
    position: absolute;
    left: 86px; top: 210px;
    width: 535px;
    font-size: 14.6px;
    line-height: 19.4px;
    color: var(--ink);
    hyphens: auto;
  }
  .letter p { margin-bottom: 19.4px; }
  .letter .salutation, .letter .signature { font-weight: 700; }

  .footer-band {
    position: absolute;
    left: 0; bottom: 0;
    width: 100%; height: 171px;
    background: var(--navy);
  }
  .sender {
    position: absolute; left: 86px; top: 26px;
  }
  .sender-name {
    font-size: 33px; font-weight: 700; color: #ffffff; line-height: 1;
  }
  .sender-role {
    margin-top: 4px;
    font-size: 13px; font-weight: 400; color: var(--gold);
    letter-spacing: 3px;
  }
  .contact {
    position: absolute; left: 436px; top: 68px;
    font-size: 8.8px; line-height: 11.5px; letter-spacing: 1.4px;
  }
  .contact-row { display: flex; }
  .contact-label {
    width: 50px; text-align: right; padding-right: 5px;
    color: var(--gold); font-weight: 400;
  }
  .contact-value { color: #ffffff; font-weight: 700; }
</style>
</head>
<body>
<div class="canvas">
  <div class="backdrop"></div>

  <article class="letterhead letterhead--primary">
    <header class="brand">
      <span class="brand-mark"></span>
      <span class="brand-name">BDN Ltd</span>
    </header>
    <section class="letter">
      <p class="salutation">Dear Ann Smith,</p>
      <p>Lorem ipsum dolor sit amet, consectetur adipiscing elit, sed do eiusmod tempor incididunt ut labore et dolore magna aliqua. Ut enim ad minim veniam, quis nostrud exercitation ullamco laboris nisi ut aliquip ex ea com modo consequat. Duis aute irure dolor in reprehenderit in voluptate velit esse cillum dolore eu fugiat nulla pariatur. Excepteur sint occaecat cupidatat non proident, sunt in culpa qui officia deserunt mollit anim id est laborum.</p>
      <p>Sed ut perspiciatis unde omnis iste natus error sit voluptatem accusantium doloremque laudantium, totam rem aperiam, eaque ipsa quae ab illo inventore veritatis et quasi architecto beatae vitae dicta sunt explicabo. Nemo enim ipsam voluptatem quia voluptas sit aspernatur aut odit aut fugit, sed quia consequuntur magni dolores eos qui ratione voluptatem sequi nesciunt. Neque porro quisquam est, qui dolorem ipsum quia dolor sit amet, consect etur, adipisci velit, sed quia non numquam eius modi tempora incidunt ut labore et dolore magnam aliquam quaerat voluptatem. Ut enim ad minima veniam, quis nostrum exercitationem ullam corporis suscipit laboriosam, nisi ut aliquid ex ea commodi consequatur?</p>
      <p>Quis autem vel eum iure reprehen erit qui in ea voluptate velit esse quam nihil molestiae consequatur, vel illum qui dolorem eum fugiat quo voluptas nulla pariatur</p>
      <p>Sincerely,</p>
      <p class="signature">John Doe</p>
    </section>
    <footer class="footer-band">
      <div class="sender">
        <div class="sender-name">John Doe</div>
        <div class="sender-role">FOUNDER</div>
      </div>
      <div class="contact">
        <div class="contact-row"><span class="contact-label">PHONE</span><span class="contact-value">+00 123 456 789</span></div>
        <div class="contact-row"><span class="contact-label">E-MAIL</span><span class="contact-value">JohnDoe@BDNLTD.com</span></div>
        <div class="contact-row"><span class="contact-label">WEB</span><span class="contact-value">www.BDNLTD.com</span></div>
      </div>
    </footer>
  </article>

  <article class="letterhead letterhead--secondary">
    <header class="brand">
      <span class="brand-mark"></span>
      <span class="brand-name">BDN Ltd</span>
    </header>
    <section class="letter">
      <p class="salutation">Dear Ann Smith,</p>
      <p>Lorem ipsum dolor sit amet, consectetur adipiscing elit, sed do eiusmod tempor incididunt ut labore et dolore magna aliqua. Ut enim ad minim veniam, quis nostrud exercitation ullamco laboris nisi ut aliquip ex ea com modo consequat. Duis aute irure dolor in reprehenderit in voluptate velit esse cillum dolore eu fugiat nulla pariatur. Excepteur sint occaecat cupidatat non proident, sunt in culpa qui officia deserunt mollit anim id est laborum.</p>
      <p>Sed ut perspiciatis unde omnis iste natus error sit voluptatem accusantium doloremque laudantium, totam rem aperiam, eaque ipsa quae ab illo inventore veritatis et quasi architecto beatae vitae dicta sunt explicabo. Nemo enim ipsam voluptatem quia voluptas sit aspernatur aut odit aut fugit, sed quia consequuntur magni dolores eos qui ratione voluptatem sequi nesciunt. Neque porro quisquam est, qui dolorem ipsum quia dolor sit amet, consect etur, adipisci velit, sed quia non numquam eius modi tempora incidunt ut labore et dolore magnam aliquam quaerat voluptatem. Ut enim ad minima veniam, quis nostrum exercitationem ullam corporis suscipit laboriosam, nisi ut aliquid ex ea commodi consequatur?</p>
      <p>Quis autem vel eum iure reprehen erit qui in ea voluptate velit esse quam nihil molestiae consequatur, vel illum qui dolorem eum fugiat quo voluptas nulla pariatur</p>
      <p>Sincerely,</p>
      <p class="signature">John Doe</p>
    </section>
    <footer class="footer-band">
      <div class="sender">
        <div class="sender-name">John Doe</div>
        <div class="sender-role">FOUNDER</div>
      </div>
      <div class="contact">
        <div class="contact-row"><span class="contact-label">PHONE</span><span class="contact-value">+00 123 456 789</span></div>
        <div class="contact-row"><span class="contact-label">E-MAIL</span><span class="contact-value">JohnDoe@BDNLTD.com</span></div>
        <div class="contact-row"><span class="contact-label">WEB</span><span class="contact-value">www.BDNLTD.com</span></div>
      </div>
    </footer>
  </article>
</div>
</body>
</html>
```